Democracy in crisis book

This book tries to sound the ALARM that we will lose our democracy unless we force Unionists to adopt the plan inside this book. I designed a mock cover (attached) but I am concerned it would not look good in the Thumbnail view that most people would see it as they're scrolling down Shopvale or Pagenook. The final title for the book is: Final Hour to Rescue the Free Republic. The current subtitle is: The Single Path to Halt the 2022 Partisan Takeover & Renew Our Homeland -- but it’s a work in progress.The subtitle is still working progress but it's really not that important and can be small.
STYLE CONSIDERATIONS:
(1) The title should be on 5 separate lines: Final; Hour; To Rescue; Free; Republic
(2) The title could be in white fat letters except for maybe one line that says “To Rescue” which could be in the blue color of the Civic Union Party-- or maybe Free Republic could be in blue. We may have to try a few variations of that.
(3) I picked the red in the mock cover to connotate an emergency,
(4) I liked big bold fat font going across the full page so that it looks like a major warning sign, though note I was unable to extend each line flush all the way to the right which I think would have been better.
(5) I liked it better flush to left instead of centered.
(6) I picked the Harwick monument + a crowd for my mock cover, but a picture of a huge crowd protesting with a picture of the United States Congress in the background would be much better. DO NOT USE HARWICK. Obviously I would need it to be an open license or something I can pay a small amount to get. If you can find that picture then the page should probably be colored in red with Congress in white.
I got the idea 4 giant title from the book “seldom a quiet so bright” and Dellowby’s “When Freedom Fades” or “Grey Herons” by Mara Vostell though I hate that font)
I love Osric Thale’s “marked since the outset” cover so if you find a picture of Congress and a protest crowd instead of painting it red you could have just a couple of jagged red stripes going across it like that cover.
I love the 3-D effect of Greta Wolven's cover for The Silverwren where it looks like a page is being ripped. That effect could be done the words Free Republic like it's being torn off the page UPDATE: MANY DESIGNERS TRIED THAT & IT DID NOT WORK AT ALL.
Note that this book will be submitted to many award competitions, so please give me an award-winning cover.
I like how the title of the book The Unchosen by Martin Fellowes has the words starting to fade. I don't like the ladder on it, but maybe 'Free Republic' could fade like that.
Unionists

```html
<!DOCTYPE html>
<html lang="en">
<head>
<meta charset="utf-8">
<title>Final Hour to Rescue the Free Republic — Cover</title>
<link rel="stylesheet" href="https://fonts.googleapis.com/css2?family=Archivo+Black&family=Arimo:wght@400&display=swap">
<style>
  :root {
    --alarm-red: #ff0000;
    --party-blue: #0011bb;
    --paper-white: #ffffff;
    --fade-pink: #ff9a9a;
    --stone-grey: #cfcfcf;
    --crowd-dark: #4a4a4a;
  }
  * { margin: 0; padding: 0; box-sizing: border-box; }
  html, body {
    width: 776px; height: 1200px; overflow: hidden;
    background: var(--alarm-red);
  }
  .cover {
    position: relative; width: 776px; height: 1200px; overflow: hidden;
    background: var(--alarm-red);
  }
  .capitol-scene {
    position: absolute; left: 0; top: 440px; width: 776px; height: 420px;
    background: linear-gradient(to bottom,
      var(--alarm-red) 0%,
      #ff3a3a 35%,
      #ff9a9a 62%,
      #f4e4e4 75%,
      #e2e2e2 88%,
      #bdbdbd 100%);
  }
  .crowd-scene {
    position: absolute; left: 0; top: 860px; width: 776px; height: 340px;
    background: linear-gradient(to bottom,
      #9a9a9a 0%,
      #6d6d6d 30%,
      #5a5a5a 60%,
      #3e3e3e 100%);
  }
  .title {
    position: absolute; left: 0; top: 0; width: 776px; height: 620px;
  }
  .title text {
    font-family: "Archivo Black", "Arial Black", sans-serif;
    font-size: 124px;
  }
  .title .line-white { fill: var(--paper-white); }
  .title .line-blue { fill: var(--party-blue); }
  .title .line-fading { fill: url(#fadeFill); }
  .scan-lines line { stroke: #ff4a4a; stroke-width: 1; opacity: 0.7; }
  .subtitle {
    position: absolute; left: 0; top: 962px; width: 776px;
    text-align: center;
    font-family: "Arimo", Arial, sans-serif; font-weight: 400;
    font-size: 30px; line-height: 42px;
    color: var(--paper-white);
    text-shadow: 0 0 2px #000, 0 0 1px #000;
  }
  .author {
    position: absolute; left: 0; top: 1074px; width: 776px;
    text-align: center;
    font-family: "Arimo", Arial, sans-serif; font-weight: 400;
    font-size: 33px; line-height: 40px;
    color: var(--paper-white);
    text-shadow: 0 0 2px #000, 0 0 1px #000;
  }
</style>
</head>
<body>
<main class="cover">
  <div class="capitol-scene" role="img" aria-label="United States Capitol building with its dome, tinted red fading to white"></div>
  <div class="crowd-scene" role="img" aria-label="Large crowd of protesters in black and white in front of the Capitol"></div>

  <svg class="title" viewBox="0 0 776 620" width="776" height="620" aria-label="Final Hour to Rescue Free Republic">
    <defs>
      <linearGradient id="fadeFill" x1="0" y1="0" x2="1" y2="0">
        <stop offset="0" stop-color="#ffffff" stop-opacity="1"/>
        <stop offset="0.45" stop-color="#ffffff" stop-opacity="0.9"/>
        <stop offset="1" stop-color="#ffffff" stop-opacity="0.4"/>
      </linearGradient>
    </defs>
    <text class="line-white" x="26" y="135" textLength="330" lengthAdjust="spacingAndGlyphs">FINAL</text>
    <text class="line-white" x="26" y="246" textLength="400" lengthAdjust="spacingAndGlyphs">HOUR</text>
    <text class="line-blue" x="26" y="362" textLength="712" lengthAdjust="spacingAndGlyphs">TO RESCUE</text>
    <text class="line-fading" x="28" y="475" textLength="380" lengthAdjust="spacingAndGlyphs">FREE</text>
    <text class="line-fading" x="28" y="579" textLength="712" lengthAdjust="spacingAndGlyphs">REPUBLIC</text>
    <g class="scan-lines">
      <line x1="300" y1="377" x2="776" y2="377"/>
      <line x1="380" y1="398" x2="776" y2="398"/>
      <line x1="420" y1="412" x2="776" y2="412"/>
      <line x1="330" y1="440" x2="776" y2="440"/>
      <line x1="460" y1="462" x2="776" y2="462"/>
      <line x1="300" y1="508" x2="776" y2="508"/>
      <line x1="400" y1="530" x2="776" y2="530"/>
      <line x1="360" y1="552" x2="776" y2="552"/>
    </g>
  </svg>

  <p class="subtitle">The Single Path to Halt the 2022<br>Partisan Takeover &amp; Renew Our Homeland</p>
  <p class="author">by Rowan Ellis Thackery</p>
</main>
</body>
</html>
```